Stationery Design Project

We are looking for a full revision of our existing stationary to include within this project:

- Letterhead
- Business card
- Compliment slip

The items should be a reflection of our new website which can be found at http://www.larkfieldchecks.co.uk/

Our logo files are included within the file brief

There are some further projects which we may approach the winning designer for as we need a revision to the front cover of our reports, a new price list and two brochures for specific target markets.

Industry/Entity Type

Business

```html
<!DOCTYPE html>
<html lang="en">
<head>
<meta charset="utf-8">
<title>Larkfield Checks – Stationery Set</title>
<link href="https://fonts.googleapis.com/css2?family=Arimo:wght@400;700&family=Archivo+Black&display=swap" rel="stylesheet">
<style>
  :root {
    --navy: #2b2a66;
    --navy-mid: #3a3f8c;
    --navy-light: #5560aa;
    --ink: #34336c;
    --paper: #fbfbf8;
    --stage-a: #f4f3f1;
    --stage-b: #dedee2;
    --name-ink: #16163a;
  }
  * { margin: 0; padding: 0; box-sizing: border-box; }
  html, body { width: 1200px; height: 729px; overflow: hidden; }
  body {
    position: relative;
    background: radial-gradient(ellipse at 78% 45%, var(--stage-a) 0%, var(--stage-b) 80%);
    font-family: "Arimo", Arial, sans-serif;
    color: var(--ink);
  }
  .sheet {
    position: absolute;
    background: var(--paper);
    box-shadow: 4px 5px 8px rgba(0,0,0,0.35);
    overflow: hidden;
  }
  address { font-style: normal; }
  .wordmark {
    font-family: "Arimo", Arial, sans-serif;
    font-weight: 700;
    color: var(--navy);
    white-space: nowrap;
    display: flex;
    align-items: center;
  }
  .wordmark .dot {
    display: inline-block;
    background: var(--navy);
    border-radius: 50%;
    margin-right: 8px;
  }

  /* Letterhead */
  .letterhead { left: 102px; top: 21px; width: 561px; height: 681px; }
  .letterhead .header-line { position: absolute; left: 0; top: 0; width: 561px; height: 150px; }
  .letterhead .wordmark { position: absolute; left: 16px; top: 42px; font-size: 26px; line-height: 30px; }
  .letterhead .wordmark .dot { width: 12px; height: 12px; }
  .letterhead .contact {
    position: absolute; right: 10px; top: 14px;
    text-align: right; font-size: 12.5px; line-height: 18px; color: var(--ink);
  }

  /* Compliment slip */
  .slip { left: 687px; top: 60px; width: 401px; height: 150px; }
  .slip .band {
    position: absolute; left: 0; top: 0; width: 100%; height: 15px;
    background: linear-gradient(90deg, var(--navy) 0%, var(--navy-mid) 60%, var(--navy-light) 100%);
    color: #fff; font-size: 12px; line-height: 15px; padding-left: 6px; letter-spacing: 0.5px;
  }
  .slip .base {
    position: absolute; left: 0; bottom: 0; width: 100%; height: 4px;
    background: linear-gradient(90deg, var(--navy), var(--navy-light));
  }
  .slip .name { position: absolute; right: 10px; top: 24px; text-align: right; }
  .slip .wordmark { position: absolute; left: 8px; bottom: 16px; font-size: 17px; }
  .slip .wordmark .dot { width: 9px; height: 9px; margin-right: 5px; }
  .slip .contact {
    position: absolute; right: 10px; bottom: 12px;
    text-align: right; font-size: 11.5px; line-height: 14px;
  }

  .name .full {
    font-family: "Archivo Black", "Arial Black", sans-serif;
    font-size: 16px; color: var(--name-ink); letter-spacing: 0.5px; line-height: 17px;
  }
  .name .role {
    font-family: "Archivo Black", "Arial Black", sans-serif;
    font-size: 10.5px; color: var(--name-ink); letter-spacing: 1px; line-height: 11px;
  }

  /* Business card front */
  .card-front { left: 690px; top: 270px; width: 335px; height: 150px; background: #fff; }
  .card-front .wordmark {
    position: absolute; left: 0; right: 0; top: 60px; justify-content: center; font-size: 24px;
  }
  .card-front .wordmark .dot { width: 12px; height: 12px; }

  /* Business card back */
  .card-back {
    left: 690px; top: 428px; width: 335px; height: 157px;
    background: linear-gradient(90deg, var(--navy) 0%, var(--navy-mid) 55%, var(--navy-light) 100%);
  }
  .card-back .name { position: absolute; right: 12px; top: 10px; text-align: right; }
  .card-back .name .full { color: #fff; font-size: 15px; }
  .card-back .name .role { color: #fff; }
  .card-back .contact {
    position: absolute; right: 12px; top: 44px;
    text-align: right; font-size: 10px; line-height: 12px; color: #c9cde8;
  }
  .card-back .swoosh { position: absolute; left: 0; bottom: 0; width: 335px; height: 60px; }
</style>
</head>
<body>

  <section class="sheet letterhead" aria-label="Letterhead">
    <svg class="header-line" viewBox="0 0 561 150" aria-hidden="true">
      <path d="M0,100 L453,124 L561,98" fill="none" stroke="var(--navy)" stroke-width="4"/>
    </svg>
    <div class="wordmark"><span class="dot"></span>LARKFIELD CHECKS</div>
    <address class="contact">
      Address: Country, Street Name<br>
      Web: larkfieldchecks.co.uk<br>
      Email: name@website.com<br>
      Phone: 000-000-000
    </address>
  </section>

  <section class="sheet slip" aria-label="Compliment slip">
    <div class="band">WITH COMPLIMENTS</div>
    <div class="name">
      <div class="full">ALAN REED</div>
      <div class="role">director</div>
    </div>
    <div class="wordmark"><span class="dot"></span>LARKFIELD CHECKS</div>
    <address class="contact">
      Address: Country, Street Name<br>
      Phone: 000-000-000<br>
      Mobile: 111-111-111
    </address>
    <div class="base"></div>
  </section>

  <section class="sheet card-front" aria-label="Business card front">
    <div class="wordmark"><span class="dot"></span>LARKFIELD CHECKS</div>
  </section>

  <section class="sheet card-back" aria-label="Business card back">
    <div class="name">
      <div class="full">ALAN REED</div>
      <div class="role">director</div>
    </div>
    <address class="contact">
      Address: Country, Street Name<br>
      Phone: 000-000-000<br>
      Mobile: 111-111-111
    </address>
    <svg class="swoosh" viewBox="0 0 335 60" aria-hidden="true">
      <path d="M0,52 C80,30 200,22 335,30" fill="none" stroke="#fff" stroke-width="2"/>
      <path d="M0,60 L0,56 C90,38 210,30 335,36 L335,60 Z" fill="rgba(255,255,255,0.12)"/>
    </svg>
  </section>

</body>
</html>
```